Simple and clean webdesign for personal homepage

Trying to create a simple and clean webdesign for my personal homepage. Going to use a static site builder with templates to build the site. I want it to have multiple pages - like an about me, blog and resume. I just need something very basic I can customize. I want the main colors to be purple, black and white. I am open to other color palettes too but since purple is my favorite color I want that to be one of the main colors.

The site be mostly text driven. Might have some images in the body text but I want the site design to be light and lean.

Industry/Entity Type

Personal Homepage.

Coding

Coded - Design and coding required

Number of Pages Required

1 page

Font styles to use
Sans Serif

Colors
6B429C
8869AF
B7A5CE
E3DAEB
F3F0F8

Requirements
Must have
• Clean design. Purple used as a color. HTML template.
Nice to have
• Responsive

```html
<!DOCTYPE html>
<html lang="en">
<head>
<meta charset="utf-8">
<title>James Holloway — Personal Homepage</title>
<link rel="stylesheet" href="https://fonts.googleapis.com/css2?family=Oswald:wght@400;600&family=Work+Sans:wght@400;500;600&family=Roboto:wght@400;500;700&display=swap">
<style>
:root{
  --purple:#5b2e91;
  --purple-mid:#7352a3;
  --purple-deep:#4a2785;
  --lilac:#eeeaf7;
  --ink:#1b1b1b;
  --text:#555;
  --white:#fff;
  --footer:#1d1d1d;
}
*{margin:0;padding:0;box-sizing:border-box}
html,body{width:1200px;height:3375px;overflow:hidden}
body{position:relative;background:var(--white);font-family:"Work Sans",sans-serif;color:var(--text)}
.abs{position:absolute}
.head-font{font-family:"Oswald",sans-serif}
.ui{font-family:"Roboto",sans-serif}

/* header */
.logo{left:110px;top:24px;font-family:"Oswald",sans-serif;font-weight:600;font-size:35px;color:var(--purple);letter-spacing:.5px}
.nav{left:446px;top:0;display:flex;gap:31px;font-family:"Roboto",sans-serif;font-weight:700;font-size:15px;color:var(--ink)}
.nav a{display:block;padding-top:36px;height:86px;text-decoration:none;color:inherit}
.nav a.active{color:var(--purple);border-top:3px solid var(--purple);padding-top:33px}
.call-box{left:891px;top:24px;width:41px;height:41px;background:var(--purple);border-radius:3px}
.call-label{left:951px;top:25px;font:700 11px "Roboto",sans-serif;color:var(--ink)}
.call-num{left:951px;top:44px;font:700 15px "Roboto",sans-serif;color:var(--purple)}

/* hero */
.hero-photo{left:0;top:86px;width:686px;height:515px;background:linear-gradient(135deg,#d8c7b0,#b9906a 50%,#7a5a3f)}
.hero-panel{left:600px;top:130px;width:600px;height:428px;background:var(--purple);color:var(--white);padding:115px 0 0 44px}
.hero-panel h1{font:600 39px "Oswald",sans-serif;letter-spacing:.3px}
.hero-panel p{font:500 16px/26px "Roboto",sans-serif;margin-top:10px;width:440px}
.btn-light{display:inline-block;margin-top:24px;background:var(--white);color:var(--purple);font:700 14px "Roboto",sans-serif;padding:16px 19px;border-radius:3px}
.socials{display:flex;align-items:center;gap:14px;margin-top:78px}
.dot{width:12px;height:12px;border-radius:50%;background:var(--white)}
.rule{width:62px;height:2px;background:var(--white);margin-left:22px}

/* sections */
.title{width:1200px;left:0;text-align:center;font:400 38px "Oswald",sans-serif;color:var(--ink)}
.title b{font-weight:600;color:var(--purple)}
.lead{left:120px;width:960px;text-align:center;font-size:14.5px;line-height:26.5px}
.btn{display:inline-block;background:var(--purple);color:var(--white);font:700 14px "Roboto",sans-serif;padding:17px 18px;border-radius:3px}

.discovery-bg{left:0;top:1099px;width:1200px;height:567px;background:var(--lilac)}
.card{top:1339px;width:232px;height:257px;background:var(--white);border-radius:4px;box-shadow:0 0 8px rgba(0,0,0,.08);text-align:center;padding-top:32px}
.card .icon{width:44px;height:44px;margin:0 auto;border:2.5px solid var(--purple);border-radius:6px}
.card h3{font:700 16px "Roboto",sans-serif;color:var(--ink);margin-top:32px;letter-spacing:.3px}
.card p{font-size:13.5px;line-height:22.5px;margin:16px 8px 0}

.features-photo{left:600px;top:1666px;width:600px;height:428px;background:linear-gradient(135deg,#2a1c14,#8a4a1e 45%,#2b3b40)}
.features-panel{left:110px;top:1738px;width:557px;height:428px;background:var(--purple-mid);color:var(--white);padding:60px 56px 0 55px}
.features-panel h2{font:400 33px "Oswald",sans-serif}
.features-panel h2 b{font-weight:600}
.features-panel ul{list-style:none;margin-top:20px}
.features-panel li{position:relative;padding-left:34px;font-size:14.5px;line-height:25px;margin-bottom:13px}
.features-panel li::before{content:"";position:absolute;left:0;top:6px;width:12px;height:12px;border-radius:50%;background:var(--white)}
.features-panel li strong{font-weight:600}

.post{top:2421px;width:476px;height:284px;background:var(--white);box-shadow:0 0 9px rgba(0,0,0,.1);border-radius:3px;padding:24px 26px}
.post h3{font:500 17px/27px "Work Sans",sans-serif;color:var(--ink)}
.meta{display:flex;align-items:center;margin-top:12px;font:500 14px "Roboto",sans-serif;color:var(--ink)}
.meta .avatar{width:14px;height:14px;border-radius:50%;border:2px solid var(--purple);margin-right:8px}
.meta .name{margin-left:14px;background:#f1f1f1;color:#666;font-family:"Work Sans",sans-serif;font-weight:400;padding:9px 20px;border-radius:3px}
.post p{font-size:14px;line-height:23px;margin-top:10px}
.post-foot{display:flex;justify-content:space-between;margin-top:22px}
.post-foot .btn{padding:16px 21px}
.follow{display:flex;align-items:center;gap:12px;background:#f1f1f1;padding:0 22px;font:500 14px "Roboto",sans-serif;color:var(--ink);border-radius:3px}
.follow i{width:9px;height:9px;border-radius:50%;background:var(--purple);display:block}

.cta{left:0;top:2800px;width:1200px;height:352px;background:linear-gradient(135deg,#5a2e95,var(--purple-deep) 55%,#5b3196);text-align:center;color:var(--white)}
.cta h2{font:400 36px "Oswald",sans-serif;margin-top:60px}
.cta h2 b{font-weight:600}
.cta p{width:930px;margin:26px auto 0;font-size:14.5px;line-height:26px}
.btn-dark{display:inline-block;margin-top:40px;background:#1a1a1a;color:var(--white);font:700 14px "Roboto",sans-serif;padding:17px 20px;border-radius:3px}

.footer{left:0;top:3152px;width:1200px;height:223px;background:var(--footer);color:var(--white)}
.f-logo{left:110px;top:78px;font:600 39px "Oswald",sans-serif;color:var(--white)}
.f-nav{right:111px;top:68px;font:700 17px "Roboto",sans-serif;display:flex;gap:22px}
.f-contact{right:111px;top:106px;font:400 14px "Roboto",sans-serif;display:flex;gap:14px;align-items:center}
.f-contact i{display:inline-block;width:9px;height:9px;border-radius:50%;background:var(--purple-mid);margin-right:8px}
.f-rule{left:111px;top:156px;width:977px;height:1px;background:#4a4a4a}
.copy{left:0;width:1200px;top:180px;text-align:center;font:400 13px "Roboto",sans-serif}
.f-social{left:1000px;top:174px;display:flex;gap:6px}
.f-social span{width:24px;height:24px;background:var(--purple)}
.f-social span:nth-child(2){background:var(--white)}
</style>
</head>
<body>

<header>
  <div class="abs logo">JAMES HOLLOWAY</div>
  <nav class="abs nav"><a class="active">HOME</a><a>ABOUT ME</a><a>RESUME</a><a>CONTACT</a></nav>
  <div class="abs call-box">
    <svg width="41" height="41" viewBox="0 0 41 41"><path d="M15 13c1-1 2-1 3 0l2 3c.5 1 0 2-1 2.5 1 2 2.5 3.5 4.5 4.5.5-1 1.5-1.5 2.5-1l3 2c1 1 1 2 0 3-2 2-4 2-7 0-3-2-5-4-7-7-2-3-2-5 0-7z" fill="#fff"/></svg>
  </div>
  <div class="abs call-label">CALL US:</div>
  <div class="abs call-num">+1 (555) 014 2290</div>
</header>

<section>
  <div class="abs hero-photo" role="img" aria-label="Photo of a smiling man working on a laptop at a desk with plants"></div>
  <div class="abs hero-panel">
    <h1>WELCOME TO JAMES HOLLOWAY</h1>
    <p>Lorem ipsum dolor sit amet consectetur adipi scing elit sed do eiusolor sit ame nsectemod.</p>
    <span class="btn-light">LEARN MORE</span>
    <div class="socials"><span class="dot"></span><span class="dot"></span><span class="dot"></span><span class="rule"></span></div>
  </div>
</section>

<section>
  <h2 class="abs title" style="top:686px">ABOUT <b>JAMES HOLLOWAY</b></h2>
  <p class="abs lead" style="top:764px">Sed ut perspiciatis unde omnis iste natus error sit voluptatem accusan tium doloremque laudantium, totam rem aperiam, eaque ipsa quae ab illo inventore veritatis et quasi architecto beatae vitae dicta sunt expl icabo. Nemo enim ipsam voluptatem quia voluptas sit aspernatur aut odit aut fugit, sed quia conseqipsam.</p>
  <p class="abs lead" style="top:863px">Perspiciatis unde omnis iste natus error sit voluptatem accusan tium doloremque laudantium, totam rem aperiam, eaque ipsa quae ab illo inventoue porro quisquam est, qui dolorem ipre veritatis et quasi architecea.</p>
  <div class="abs" style="left:0;width:1200px;top:953px;text-align:center"><span class="btn">LEARN MORE</span></div>
</section>

<section>
  <div class="abs discovery-bg"></div>
  <h2 class="abs title" style="top:1156px">OUR <b>DISCOVERY</b></h2>
  <p class="abs lead" style="top:1222px">Sed ut perspiciatis unde omnis iste natus error sit voluptatem accusan tium doloremque laudantium, totam rem aperiam, eaque ipsa quae ab illo inventore veritatis et quasi archites iste natus error sit voluptatem accusan tium doloremque laudantium, totam rem aperiam, eaque ipsa quae ab illo architeccto beatae vitae dicta sunt expl icabo.</p>
  <div class="abs card" style="left:111px"><div class="icon"></div><h3>LEADERSHIP</h3><p>Sed ut perspiciatis unde omn is iste natus error sit volu ptatem accusan tium dolore mqus erroue.</p></div>
  <div class="abs card" style="left:360px"><div class="icon"></div><h3>FRIENDLY SUPPORT</h3><p>Sed ut perspiciatis unde omn is iste natus error sit volu ptatem accusan tium dolore mqus erroue.</p></div>
  <div class="abs card" style="left:608px"><div class="icon"></div><h3>PERSONAL TRAINER</h3><p>Sed ut perspiciatis unde omn is iste natus error sit volu ptatem accusan tium dolore mqus erroue.</p></div>
  <div class="abs card" style="left:857px"><div class="icon"></div><h3>RESUME &amp; CV</h3><p>Sed ut perspiciatis unde omn is iste natus error sit volu ptatem accusan tium dolore mqus erroue.</p></div>
</section>

<section>
  <div class="abs features-photo" role="img" aria-label="Photo of a developer working at two monitors showing code in a dim warm room"></div>
  <div class="abs features-panel">
    <h2>OUR <b>FEATURES</b></h2>
    <ul>
      <li><strong>Quick scheduling:</strong> Unde omnis iste natus error sit volup tatem accusan tium doloremque laudantium.</li>
      <li><strong>Recordings:</strong> Unde omnis iste natus error sit voluptatem accusan tium dolorea.</li>
      <li><strong>Security:</strong> Unde omnis iste natus error sit voluptatem laudantium.</li>
      <li><strong>Analytics:</strong> Unde omnis iste natus error sit voluptatem accusan tium doloremque laudantium.</li>
    </ul>
  </div>
</section>

<section>
  <h2 class="abs title" style="top:2248px">LATEST <b>BLOG</b></h2>
  <p class="abs lead" style="top:2323px;left:130px;width:940px">Sed ut perspiciatis unde omnis iste natus error sit voluptatem accusan tium doloremque laudantium, totam rem aperiam, eaque ipsa quae ab illo inventore veritatis et quasi architecto beatae vitae dicta sunt expl icabo.</p>
  <article class="abs post" style="left:111px">
    <h3>Lorem ipsum dolor sit amet consectetur adipis cing eiusmod tempor incidiea</h3>
    <div class="meta"><span class="avatar"></span>AUTHOR:<span class="name">James Holloway</span></div>
    <p>Sed ut perspiciatis unde omnis iste natus error sit volupta tem accusantium doloremque laudantium, totam rem aperiam, eaque ipsa quae ab illo invea.</p>
    <div class="post-foot"><span class="btn">VIEW POST</span><span class="follow">Follow Us: <i></i><i></i><i></i></span></div>
  </article>
  <article class="abs post" style="left:611px">
    <h3>Lorem ipsum dolor sit amet consectetur adipis cing eiusmod tempor incidiea</h3>
    <div class="meta"><span class="avatar"></span>AUTHOR:<span class="name">James Holloway</span></div>
    <p>Sed ut perspiciatis unde omnis iste natus error sit volupta tem accusantium doloremque laudantium, totam rem aperiam, eaque ipsa quae ab illo invea.</p>
    <div class="post-foot"><span class="btn">VIEW POST</span><span class="follow">Follow Us: <i></i><i></i><i></i></span></div>
  </article>
</section>

<section class="abs cta">
  <h2>GET READY <b>TO START?</b></h2>
  <p>Sed ut perspiciatis unde omnis iste natus error sit voluptatem accusantium doloremque laudantium, totam rem aperiam, eaque ipsa quae ab illo inventore veritatis et quasi architecto beatae vitae dicta sunt explicabo. Nemo enim ipsam voluptatem quia voluptas sit aspernatur aut odit aut fugit, sed quia consequunturea.</p>
  <span class="btn-dark">CONTACT NOW</span>
</section>

<footer class="abs footer">
  <div class="abs f-logo">JAMES HOLLOWAY</div>
  <nav class="abs f-nav"><span>HOME</span><span>|</span><span>ABOUT ME</span><span>|</span><span>RESUME</span><span>|</span><span>CONTACT</span></nav>
  <div class="abs f-contact"><span><i></i>+1 (555) 014 2290</span><span>|</span><span><i></i>info@jamesholloway.com</span></div>
  <div class="abs f-rule"></div>
  <div class="abs copy">© 2022 <b>JAMES HOLLOWAY</b> &nbsp;|&nbsp; All Rights Reserved</div>
  <div class="abs f-social"><span></span><span></span><span></span></div>
</footer>

</body>
</html>
```